Dallas Texas Special Event Center Flyer

Need a new brochure (small 8.5 x 11 tri-fold) for an event center in Dallas, Texas area. It is located on a golf course and is ideal for weddings, quinceaneras, retirement parties, etc. Is best known for weddings. There is no logo for the event center. I have attached the prior brochure, which is not professional. We do not have any site photos.

Target Market(s)

people seeking special event space in dallas, texas area. Brides, meeting planners, etc.

Industry/Entity Type

Golf Course

Font styles to use
Script
Other font styles liked:
• combine serif and some use of script ok

Requirements
Must have
• lots of photos - see attached

```html
<!DOCTYPE html>
<html lang="en">
<head>
<meta charset="utf-8">
<title>Event Center at Willowbend – Tri-fold Brochure</title>
<link rel="stylesheet" href="https://fonts.googleapis.com/css2?family=Cinzel:wght@400;700&family=Crimson+Text:wght@400;700&family=Dancing+Script:wght@500&display=swap">
<style>
  :root {
    --gold-deep: #d9a93f;
    --gold-mid: #ecc66e;
    --gold-pale: #f6e2aa;
    --cream: #fbf1d8;
    --ink: #2a2218;
    --ink-soft: #3a3024;
    --rule: #8a6a28;
    --photo-table-a: #efe6dc;
    --photo-table-b: #d9c4a4;
    --photo-couple-a: #f3ead0;
    --photo-couple-b: #8c9a5c;
    --photo-couple-c: #5d6b3a;
    --photo-flowers-a: #e7c98f;
    --photo-flowers-b: #8d6a3c;
    --photo-toast-a: #d7b58a;
    --photo-toast-b: #7a5238;
  }
  * { box-sizing: border-box; margin: 0; padding: 0; }
  html, body { width: 1200px; height: 924px; overflow: hidden; background: #ffffff; }
  .brochure { display: flex; width: 1200px; height: 924px; }
  .panel { position: relative; width: 400px; height: 924px; overflow: hidden; }

  /* Left panel */
  .panel--about { background: linear-gradient(180deg, var(--gold-pale) 0%, var(--gold-mid) 55%, #e4b763 100%); }
  .photo { position: absolute; left: 0; width: 100%; }
  .photo--table {
    top: 0; height: 330px;
    background: radial-gradient(ellipse at 20% 25%, #e9d7de 0%, transparent 35%),
                linear-gradient(180deg, var(--photo-table-a) 0%, var(--photo-table-b) 70%, rgba(236,198,110,0) 100%);
  }
  .about-box {
    position: absolute; left: 11px; top: 277px; width: 377px; bottom: 0;
    background: rgba(251, 236, 196, 0.62);
    border-radius: 6px 6px 0 0;
    padding: 24px 12px 0 13px;
  }
  .about-box p {
    font-family: "Crimson Text", Georgia, serif;
    font-size: 16.5px; line-height: 24.5px; color: var(--ink-soft);
    margin-bottom: 24px;
  }
  .about-box strong { font-weight: 700; color: var(--ink); }

  /* Middle panel */
  .panel--contact {
    background: linear-gradient(180deg, var(--gold-mid) 0%, var(--gold-deep) 35%, #e3b657 60%, var(--gold-pale) 72%);
    text-align: center; font-family: "Crimson Text", Georgia, serif; color: var(--ink);
  }
  .contact-title { font-family: "Cinzel", Georgia, serif; font-weight: 400; margin-top: 47px; line-height: 1; }
  .contact-title .big { display: block; font-size: 23px; letter-spacing: 1px; }
  .contact-title .small { display: block; font-size: 16px; letter-spacing: 1px; margin-top: 6px; }
  .contact-rule {
    width: 240px; height: 1px; margin: 10px auto 0;
    background: linear-gradient(90deg, transparent, var(--rule), transparent);
  }
  .contact-lines { font-size: 16.5px; line-height: 25.5px; margin-top: 20px; }
  .contact-lines + .contact-lines { margin-top: 25px; }
  .contact-about { font-size: 16.5px; line-height: 25.5px; margin: 25px 12px 0; }
  .contact-visit { font-size: 16.5px; line-height: 25.5px; margin-top: 25px; }
  .contact-visit .url { font-weight: 700; }
  .photo--flowers {
    bottom: 0; height: 300px;
    background: radial-gradient(ellipse at 50% 50%, #c8864d 0%, transparent 45%),
                linear-gradient(180deg, rgba(246,226,170,0) 0%, var(--photo-flowers-a) 25%, var(--photo-flowers-b) 100%);
  }

  /* Right panel */
  .panel--cover { background: var(--cream); }
  .photo--couple {
    top: 0; height: 650px;
    background: radial-gradient(ellipse at 55% 65%, #efe7dc 0%, transparent 30%),
                linear-gradient(180deg, var(--photo-couple-a) 0%, #e7d8a8 30%, var(--photo-couple-b) 60%, var(--photo-couple-c) 100%);
  }
  .cover-title {
    position: absolute; top: 48px; left: 0; width: 100%; text-align: center;
    font-family: "Cinzel", Georgia, serif; color: #111; font-weight: 400; line-height: 1;
  }
  .cover-title .line1 { display: block; font-size: 36px; letter-spacing: 1px; }
  .cover-title .line2 { display: block; font-size: 54px; margin-top: 4px; }
  .tagline-band {
    position: absolute; top: 660px; left: 0; width: 100%; height: 106px;
    background: linear-gradient(180deg, var(--gold-pale), var(--gold-mid) 60%, var(--gold-deep));
    display: flex; align-items: center; justify-content: center; text-align: center;
  }
  .tagline-band::before, .tagline-band::after {
    content: ""; position: absolute; left: 0; right: 0; border-top: 1.5px dashed var(--rule);
  }
  .tagline-band::before { top: 5px; }
  .tagline-band::after { bottom: 5px; }
  .tagline { font-family: "Dancing Script", cursive; font-weight: 500; font-size: 31px; line-height: 38px; color: var(--ink); }
  .photo--toast {
    top: 766px; height: 158px;
    background: radial-gradient(ellipse at 65% 60%, #f1e6c4 0%, transparent 40%),
                linear-gradient(135deg, var(--photo-toast-a), var(--photo-toast-b));
  }
</style>
</head>
<body>
<main class="brochure">
  <section class="panel panel--about">
    <div class="photo photo--table" role="img" aria-label="Banquet table set with a floral centerpiece, glassware and white linens"></div>
    <div class="about-box">
      <p>The Event Center at Willowbend offers a 12,000 square foot facility which boasts a Grand Ballroom and two Banquet Rooms.</p>
      <p><strong>The grand ballroom</strong> will accommodate 809 guests for a weeding ceremony and reception.</p>
      <p>The bridal suite at top of the winding staircase allow the Bride and her bridemaids to get ready out of site of arriving guests.</p>
      <p><strong>Banquet Room 1</strong> will accommodate 103 guests for a small, private event while <strong>Banquet Room 2</strong> will accommodate 35 guests. These two rooms can be used separately or together.</p>
      <p>The Event Center has a full commercial kitchen onsite to cater any event from formal dining to buffet-style. The menu can be customized to your specifications and will be prepared by our chef and his staff.</p>
      <p>The Event Center at Willowbend is the perfect location for your wedding, conference, seminar, party, reunion, or graduation.</p>
    </div>
  </section>

  <section class="panel panel--contact">
    <h2 class="contact-title"><span class="big">Contact Us</span><span class="small">for more information</span></h2>
    <div class="contact-rule"></div>
    <p class="contact-lines">Carla Denton<br>carla@eventcenteratwillowbend.com<br>214-555-0147<br>972-555-0192</p>
    <p class="contact-lines">Event Center at Willowbend<br>2418 County Road 90<br>Maplewood, TX 75000</p>
    <p class="contact-about">The Event Center at Willowbend is located on Willowbend Golf Course, an 18-hole, 215-acre Championship golf course in Maplewood, Texas, and is surrounded by rolling hills, seven lakes, creeks, pecan orchards, and many varieties of wildlife.</p>
    <p class="contact-visit">Visit us at:<br><span class="url">www.eventcenteratwillowbend.com</span></p>
    <div class="photo photo--flowers" role="img" aria-label="Floral centerpiece of roses and greenery on a reception table with glassware"></div>
  </section>

  <section class="panel panel--cover">
    <div class="photo photo--couple" role="img" aria-label="Bride and groom walking outdoors as guests toss petals"></div>
    <h1 class="cover-title"><span class="line1">Event Center at</span><span class="line2">WILLOWBEND</span></h1>
    <div class="tagline-band"><p class="tagline">The Premiere Event Center<br>in the Dallas area</p></div>
    <div class="photo photo--toast" role="img" aria-label="Guests raising champagne glasses in a toast"></div>
  </section>
</main>
</body>
</html>
```